Business Card Design

Mortgage brokering company, also providing Commercial Finance, Car Finance and Insurance.

Target Market(s)

Home Buyers

Industry/Entity Type

Business

Contact Information for Business Card

All information required on business card is contained in the attachment. Design does not have to follow the style of the attachment.

```html
<!DOCTYPE html>
<html lang="en">
<head>
<meta charset="utf-8">
<title>BRN Lending Services – Business Card</title>
<link href="https://fonts.googleapis.com/css2?family=Montserrat:wght@300&family=PT+Sans:ital,wght@0,400;0,700;1,400&display=swap" rel="stylesheet">
<style>
  :root {
    --backdrop: #2b2b2b;
    --navy: #1d2f39;
    --paper: #f4f4f4;
    --ink: #1d2f39;
    --muted: #5a5f63;
    --white: #ffffff;
    --soft-white: #c9d2d6;
    --accent: #e0782a;
  }
  * { box-sizing: border-box; margin: 0; padding: 0; }
  html, body { width: 1200px; height: 900px; overflow: hidden; }
  body { background: var(--backdrop); position: relative; }

  .card {
    position: absolute;
    left: 230px;
    width: 740px;
    height: 420px;
    overflow: hidden;
    box-shadow: 0 8px 24px rgba(0,0,0,.45);
  }

  /* Reverse side */
  .card--back { top: 20px; background: var(--navy); }
  .back-mark {
    position: absolute; left: 0; right: 0; top: 110px;
    display: flex; flex-direction: column; align-items: center; gap: 36px;
  }
  .back-mark__dot { width: 110px; height: 110px; border-radius: 50%; background: var(--soft-white); }
  .back-mark__name {
    font-family: "Montserrat", sans-serif; font-weight: 300;
    font-size: 30px; letter-spacing: 1.5px; color: var(--soft-white);
  }

  /* Front side */
  .card--front { top: 460px; background: var(--paper); }
  .front-title {
    position: absolute; left: 48px; top: 40px;
    font-family: "Montserrat", sans-serif; font-weight: 300;
    font-size: 30px; letter-spacing: 1.5px; color: var(--ink);
  }
  .front-band {
    position: absolute; left: 0; right: 0; top: 100px; height: 200px;
    background: var(--navy);
  }
  .contact {
    position: absolute; left: 48px; top: 128px;
    font-family: "PT Sans", sans-serif; color: var(--white);
  }
  .contact__name { font-weight: 700; font-size: 22px; }
  .contact__role { font-style: italic; font-size: 16px; font-weight: 400; }
  .contact__list { list-style: none; margin-top: 12px; font-size: 13.5px; line-height: 19px; color: var(--soft-white); }
  .divider { position: absolute; left: 400px; top: 130px; }
  .front-mark {
    position: absolute; left: 510px; top: 60px;
    width: 190px; height: 190px; border-radius: 50%;
    background: var(--accent);
  }
  .front-web {
    position: absolute; left: 0; right: 0; top: 340px; text-align: center;
    font-family: "Montserrat", sans-serif; font-weight: 300;
    font-size: 20px; letter-spacing: 4px; color: var(--muted);
  }
</style>
</head>
<body>
  <section class="card card--back" aria-label="Card reverse">
    <div class="back-mark">
      <span class="back-mark__dot"></span>
      <span class="back-mark__name">BRN Lending Services</span>
    </div>
  </section>

  <section class="card card--front" aria-label="Card front">
    <h1 class="front-title">BRN Lending Services</h1>
    <div class="front-band"></div>
    <div class="contact">
      <p><span class="contact__name">Martin Hale</span> <span class="contact__role">– Credit representative</span></p>
      <ul class="contact__list">
        <li>Address: 14 Harbour Lane, Coral Bay, Qld 4300</li>
        <li>Mobile: 0400123456</li>
        <li>Phone/Fax: 0700123456</li>
        <li>Email: martin.hale@brnlending.com.au</li>
      </ul>
    </div>
    <svg class="divider" width="12" height="150" viewBox="0 0 12 150" aria-hidden="true">
      <line x1="10" y1="0" x2="2" y2="150" stroke="#ffffff" stroke-width="1.5"/>
    </svg>
    <span class="front-mark" aria-hidden="true"></span>
    <p class="front-web">www.brnlending.com.au</p>
  </section>
</body>
</html>
```